Wellness product startup company needs packing design

We are starting up with a range of wellness products and looking for colorful, modern & trendy designs, highlighting the brand and product name as bold & prominent as possible.
sending few samples which I tried to design myself. not at all happy with the result though.
Also please use colors that go well with the Health & Wellness products (these products also comes under food supplement range)
Target Market(s)
India
Industry/Entity Type
Health And Wellness
Font styles to use
Serif
Colors
9bcb3b
f37122
e34197
Requirements
Must have
- Prominent logo & product name
Nice to have
- I leave it to you.
Should not have
- I leave it to designer.

```html
<!DOCTYPE html>
<html lang="en">
<head>
<meta charset="utf-8">
<title>Vitality Grove – Zestful+ Label</title>
<link href="https://fonts.googleapis.com/css2?family=Arimo:wght@400;700&display=swap" rel="stylesheet">
<style>
  :root {
    --backdrop: #eeeeee;
    --label-white: #ffffff;
    --brand-green: #8dbb2c;
    --tagline-grey: #555555;
    --product-red: #c7304f;
    --pink-deep: #e46a80;
    --pink-mid: #f19aa8;
    --pink-light: #fbd3da;
    --pill-red: #c42c4c;
    --body-text: #444444;
  }
  html, body {
    margin: 0;
    padding: 0;
    width: 1200px;
    height: 1000px;
    overflow: hidden;
    background: var(--backdrop);
    font-family: "Arimo", Arial, sans-serif;
  }
  .canvas {
    position: relative;
    width: 1200px;
    height: 1000px;
  }
  .label {
    position: absolute;
    left: 220px;
    top: 220px;
    width: 760px;
    height: 560px;
    background: var(--label-white);
    box-shadow: 0 2px 10px rgba(0,0,0,0.08);
    overflow: hidden;
  }
  .front-panel {
    position: absolute;
    left: 0;
    top: 0;
    width: 560px;
    height: 560px;
  }
  .band-top {
    position: absolute;
    left: 0; top: 0;
    width: 760px;
    height: 70px;
    background: linear-gradient(100deg, var(--pink-deep) 0%, var(--pink-mid) 45%, var(--pink-light) 70%, var(--pink-mid) 100%);
  }
  .band-bottom {
    position: absolute;
    left: 0; top: 250px;
    width: 560px;
    height: 310px;
    background: linear-gradient(160deg, var(--pink-deep) 0%, var(--pink-mid) 30%, var(--pink-light) 55%, var(--pink-mid) 80%, var(--pink-deep) 100%);
  }
  .brand {
    position: absolute;
    left: 0;
    top: 120px;
    width: 560px;
    text-align: center;
  }
  .brand-name {
    display: inline-flex;
    align-items: center;
    gap: 10px;
    font-size: 38px;
    font-weight: 700;
    line-height: 44px;
    color: var(--brand-green);
  }
  .brand-dot {
    width: 14px;
    height: 14px;
    border-radius: 50%;
    background: var(--brand-green);
  }
  .tagline {
    margin-top: 6px;
    font-size: 14px;
    font-weight: 400;
    color: var(--tagline-grey);
  }
  .category {
    position: absolute;
    left: 0;
    top: 214px;
    width: 560px;
    text-align: center;
    font-size: 15px;
    color: var(--brand-green);
    font-weight: 700;
  }
  .product {
    position: absolute;
    left: 0;
    top: 300px;
    width: 560px;
    text-align: center;
  }
  .product-name {
    font-size: 54px;
    font-weight: 700;
    color: var(--product-red);
  }
  .product-name sup {
    font-size: 34px;
    vertical-align: 24px;
  }
  .product-ingredients {
    margin-top: 2px;
    font-size: 12px;
    font-weight: 700;
    color: var(--tagline-grey);
  }
  .pack-pill {
    position: absolute;
    left: 208px;
    top: 482px;
    width: 144px;
    height: 24px;
    border-radius: 6px;
    border: 1.5px solid var(--label-white);
    background: var(--pill-red);
    color: var(--label-white);
    font-size: 11px;
    font-weight: 700;
    letter-spacing: 0.5px;
    line-height: 21px;
    text-align: center;
    box-sizing: border-box;
  }
  .side-panel {
    position: absolute;
    left: 560px;
    top: 70px;
    width: 200px;
    height: 490px;
    border-left: 1px solid #eeeeee;
    box-sizing: border-box;
    padding: 50px 18px 0;
    font-size: 12px;
    line-height: 19px;
    color: var(--body-text);
  }
  .side-panel .heading {
    font-weight: 700;
  }
  .side-panel p {
    margin: 0;
  }
  .side-panel .note {
    margin-top: 14px;
  }
</style>
</head>
<body>
<main class="canvas">
  <section class="label">
    <div class="band-top" role="img" aria-label="Pink geometric pattern band"></div>
    <div class="front-panel">
      <div class="band-bottom" role="img" aria-label="Pink geometric chevron pattern"></div>
      <div class="brand">
        <div class="brand-name"><span class="brand-dot"></span>VITALITY GROVE</div>
        <div class="tagline">Everyday natural care</div>
      </div>
      <div class="category">Daily Energy Booster</div>
      <div class="product">
        <div class="product-name">Zestful<sup>+</sup></div>
        <div class="product-ingredients">(with ashwagandha, shilajit &amp; ginseng)</div>
      </div>
      <div class="pack-pill">Pack of 60 capsules</div>
    </div>
    <aside class="side-panel">
      <p class="heading">Ingredients:</p>
      <p>Ashwagandha extract 250 mg</p>
      <p>Shilajit extract 150 mg</p>
      <p>Ginseng extract 100 mg</p>
      <p class="note">Dosage: 1 capsule twice daily</p>
      <p>Store in a cool, dry place</p>
      <p class="note heading">Made in India</p>
    </aside>
  </section>
</main>
</body>
</html>
```